RW Soundworks Web Site Design

Need a basic site to show clients a little about what we do. We are a custom audio video company in the high-end residential market. Need a few basic but professional pages to show past projects and products we sell. No e-commerce. Should include my new logo from MarkHive.

Industry/Entity Type

Residential

Number of Pages Required

2 page

Font styles to use
Serif
Sans Serif

Colors
f78f20

Requirements
Must have
• Company Logo, Send feedback page
Nice to have
• I have no ideas about design, but I do know what I like and dislike when I see it.

```html
<!DOCTYPE html>
<html lang="en">
<head>
<meta charset="utf-8">
<title>RW Soundworks</title>
<link href="https://fonts.googleapis.com/css2?family=Oswald:wght@400;500&family=Lato:wght@400;700&display=swap" rel="stylesheet">
<style>
:root{
  --orange:#f78f20;
  --orange-dark:#d9740c;
  --ink:#222;
  --text:#666;
  --grey-band:#ebebe9;
  --grey-light:#f3f3f2;
  --dark:#1f1f1f;
  --darker:#151515;
  --icon:#777;
}
*{margin:0;padding:0;box-sizing:border-box}
html,body{width:1200px;height:2209px;overflow:hidden}
body{position:relative;background:#fff;font-family:"Lato",sans-serif;color:var(--text)}
.abs{position:absolute}
.head{font-family:"Oswald",sans-serif;font-weight:500;text-transform:uppercase;color:var(--ink)}
.head span{color:var(--orange)}
.brand{font-family:"Oswald",sans-serif;font-weight:500;font-size:30px;color:var(--ink);display:flex;align-items:center;gap:12px}
.brand i{display:block;width:26px;height:26px;background:var(--orange)}
.top-contact{display:flex;align-items:center;gap:14px}
.diamond{width:44px;height:44px;display:flex;align-items:center;justify-content:center}
.diamond svg{display:block}
.top-contact small{display:block;font-size:12px;color:#999}
.top-contact b{font-weight:400;font-size:17px;color:#333}
.nav{top:101px;left:0;width:1200px;height:47px;background:var(--orange);border-bottom:2px solid var(--orange-dark)}
.nav ul{list-style:none;position:absolute;left:131px;top:0;display:flex;height:45px}
.nav li{font-size:15px;color:#2a2a2a;line-height:45px;padding:0 26px;position:relative}
.nav li+li:before{content:"";position:absolute;left:0;top:17px;height:12px;width:1px;background:#b86a16}
.nav li.active{background:#222;color:#fff;padding:0 22px}
.nav li.active+li:before{display:none}
.hero{top:148px;left:0;width:1200px;height:424px;background:linear-gradient(180deg,#d9d4cf 0%,#a39e98 55%,#3a3532 100%)}
.hero-band{top:480px;left:0;width:1200px;height:92px;background:rgba(25,25,25,.75)}
.hero-title{top:490px;left:133px;width:300px;font-family:"Oswald",sans-serif;font-size:29px;line-height:34px;color:#fff}
.hero-title em{font-style:normal;color:var(--orange)}
.hero-text{top:498px;left:478px;width:600px;font-size:18px;line-height:27px;color:#fff}
.arrow{width:37px;height:36px;background:rgba(210,210,210,.85);display:flex;align-items:center;justify-content:center}
.section-title{font-size:30px;width:1200px;text-align:center;letter-spacing:.5px}
.card{width:216px;height:281px;background:var(--orange)}
.card .photo{height:159px}
.card h3{font-family:"Oswald",sans-serif;font-weight:400;font-size:16px;color:#fff;margin:12px 10px 10px}
.card p{font-size:12px;line-height:18px;color:#fbe3c6;margin:0 10px}
.card a{display:block;font-size:10px;color:#2a2a2a;margin:10px 10px 0}
.about{top:992px;left:0;width:611px;height:365px;background:var(--grey-band)}
.team{top:992px;left:611px;width:589px;height:365px;background:var(--grey-light)}
.about p{font-size:12.5px;line-height:20px;color:#777;width:445px}
.btn{background:var(--orange);color:#333;font-size:11px;border-bottom:2px solid var(--orange-dark)}
.member h4{font-family:"Oswald",sans-serif;font-weight:400;font-size:17px;color:var(--orange)}
.member em{display:block;font-size:12px;color:#888;margin:2px 0 6px}
.member p{font-size:12.5px;line-height:20px;color:#777;width:300px}
.project .photo{width:216px;height:159px}
.project h3{font-family:"Oswald",sans-serif;font-weight:400;font-size:17px;color:var(--orange);margin-top:10px}
.contact{top:1677px;left:0;width:1200px;height:483px;background:var(--dark)}
.footer{top:2160px;left:0;width:1200px;height:49px;background:var(--darker);color:#bbb;font-size:12.5px;text-align:center;line-height:49px}
.col-title{font-family:"Oswald",sans-serif;font-weight:400;font-size:17px;color:#fff}
.field{width:381px;height:42px;background:#fff;border-radius:3px;font-size:15px;color:#888;padding:11px 13px}
.submit{width:119px;height:42px;background:var(--orange);color:#fff;font-family:"Oswald",sans-serif;font-size:18px;text-align:center;line-height:42px}
.detail{display:flex;align-items:center;gap:12px;font-size:13px;line-height:19px;color:#ddd}
.detail .diamond{flex:none}
.social{display:flex;align-items:center;gap:18px;font-size:12px;color:#ccc;letter-spacing:.5px}
</style>
</head>
<body>

<header>
  <div class="abs brand" style="top:34px;left:131px"><i></i>RW Soundworks</div>
  <div class="abs top-contact" style="top:24px;left:660px">
    <div class="diamond"><svg width="44" height="44" viewBox="0 0 44 44"><rect x="8" y="8" width="28" height="28" rx="4" transform="rotate(45 22 22)" fill="var(--icon)"/><path d="M17 16c1-1 2-1 3 0l2 3-2 2c1 2 2 3 4 4l2-2 3 2c1 1 1 2 0 3-4 3-15-8-12-12z" fill="#fff"/></svg></div>
    <div><small>Call Us</small><b>(555)-201-4830</b></div>
  </div>
  <div class="abs top-contact" style="top:24px;left:884px">
    <div class="diamond"><svg width="44" height="44" viewBox="0 0 44 44"><rect x="8" y="8" width="28" height="28" rx="4" transform="rotate(45 22 22)" fill="var(--icon)"/><rect x="15" y="17" width="14" height="10" fill="#fff"/><path d="M15 17l7 6 7-6" stroke="var(--icon)" stroke-width="1.5" fill="none"/></svg></div>
    <div><small>Email Us</small><b>info@rwsoundworks.com</b></div>
  </div>
</header>

<nav class="abs nav">
  <ul>
    <li class="active">HOME</li><li>OUR TEAM</li><li>PRODUCTS</li><li>OUR SERVICES</li><li>PAST PROJECT</li><li>FEEDBACK</li><li>CONTACT US</li>
  </ul>
</nav>

<section>
  <div class="abs hero" role="img" aria-label="Living room home theatre with tall floor speakers and a wall television"></div>
  <div class="abs arrow" style="top:344px;left:6px"><svg width="12" height="14"><path d="M9 2L3 7l6 5" stroke="#222" stroke-width="3" fill="none"/></svg></div>
  <div class="abs arrow" style="top:344px;left:1157px"><svg width="12" height="14"><path d="M3 2l6 5-6 5" stroke="#222" stroke-width="3" fill="none"/></svg></div>
  <div class="abs hero-band"></div>
  <div class="abs" style="top:480px;left:0;width:450px;height:92px;background:rgba(15,15,15,.6)"></div>
  <h1 class="abs hero-title" style="font-weight:500">Welcome to<br><em>RW Soundworks</em></h1>
  <p class="abs hero-text">We expert in Residential Cinemas Make your Home Safe &amp; Secure With our largest audio video control system</p>
</section>

<section>
  <h2 class="abs head section-title" style="top:610px;left:0"><span>Our</span> Services</h2>
  <div class="abs arrow" style="top:796px;left:94px"><svg width="12" height="14"><path d="M9 2L3 7l6 5" stroke="#fff" stroke-width="2.5" fill="none"/></svg></div>
  <div class="abs arrow" style="top:796px;left:1068px"><svg width="12" height="14"><path d="M3 2l6 5-6 5" stroke="#fff" stroke-width="2.5" fill="none"/></svg></div>
  <article class="abs card" style="top:674px;left:131px"><div class="photo" role="img" aria-label="Dark red home cinema room with recliner seats" style="background:linear-gradient(160deg,#7a2b22,#2a1210)"></div><h3>Residential Cinemas</h3><p>Lor ipsumdolorsitac nsectetur adipiscing elit d.uis.</p><a>View Details »</a></article>
  <article class="abs card" style="top:674px;left:371px"><div class="photo" role="img" aria-label="Consultant and client reviewing plans on a laptop" style="background:linear-gradient(160deg,#e4d3b8,#8a7b6a)"></div><h3>Design And Consultations</h3><p>Lor ipsumdolorsitac nsectetur adipiscing elit d.uis.</p><a>View Details »</a></article>
  <article class="abs card" style="top:674px;left:612px"><div class="photo" role="img" aria-label="Hand holding a remote control in a lounge" style="background:linear-gradient(160deg,#b89a84,#5a3a2c)"></div><h3>Automated Lighting Control</h3><p>Lor ipsumdolorsitac nsectetur adipiscing elit d.uis.</p><a>View Details »</a></article>
  <article class="abs card" style="top:674px;left:852px"><div class="photo" role="img" aria-label="Outdoor television mounted on a stone wall" style="background:linear-gradient(160deg,#8a7f70,#4e463c)"></div><h3>Outdoor Audio and Video</h3><p>Lor ipsumdolorsitac nsectetur adipiscing elit d.uis.</p><a>View Details »</a></article>
</section>

<section class="abs about">
  <div class="abs" style="top:40px;left:131px;display:flex;align-items:center;gap:14px">
    <h2 class="head" style="font-size:30px"><span>About</span></h2>
    <div style="width:2px;height:40px;background:#222"></div>
    <div class="brand" style="font-size:18px;gap:8px"><i style="width:14px;height:14px"></i>RW Soundworks</div>
  </div>
  <p class="abs" style="top:100px;left:131px">Lorem ipsum dolor sit amet, consectetuer adipiscing elit, sed diam nonummy nibh euismod tincidunt ut laoreet dolore magna aliquam erat volutpat. Ut wisi enim ad minim veniam, quis nostrud exerci tation ullamcorper suscipit lobortis nisl ut aliquip ex ea commodo consequat.</p>
  <p class="abs" style="top:198px;left:131px">Duis autem vel eum iriure dolor in hendrerit in vulputate velit esse molestie consequat, vel illum dolore eu feugiat nulla facilisis at vero eros et accumsan et iusto odio dignissim qui blandit praesent luptatum zzril delenit augue duis dolore te feugait nulla facilisi.</p>
  <div class="abs btn" style="top:291px;left:131px;width:94px;height:32px;line-height:30px;text-align:center">Read More »</div>
</section>

<section class="abs team">
  <h2 class="abs head" style="top:40px;left:46px;font-size:30px"><span>Our</span> Team</h2>
  <svg class="abs" style="top:105px;left:40px" width="84" height="84" role="img" aria-label="Portrait of Dale Marsh"><rect x="14" y="14" width="56" height="56" rx="8" transform="rotate(45 42 42)" fill="#c9c9c6"/></svg>
  <div class="abs member" style="top:106px;left:152px"><h4>Dale Marsh</h4><em>Director</em><p>Ut wisi enim ad minim veniam, quis nostrud exerci tation ullamcorper suscipit lobortis nisl ut aliquip.</p></div>
  <svg class="abs" style="top:227px;left:40px" width="84" height="84" role="img" aria-label="Portrait of Nina Forde"><rect x="14" y="14" width="56" height="56" rx="8" transform="rotate(45 42 42)" fill="#c9c9c6"/></svg>
  <div class="abs member" style="top:228px;left:152px"><h4>Nina Forde</h4><em>Director</em><p>Ut wisi enim ad minim veniam, quis nostrud exerci tation ullamcorper suscipit lobortis nisl ut aliquip.</p></div>
</section>

<section>
  <h2 class="abs head section-title" style="top:1398px;left:0"><span>Past</span> Project</h2>
  <div class="abs arrow" style="top:1523px;left:94px"><svg width="12" height="14"><path d="M9 2L3 7l6 5" stroke="#fff" stroke-width="2.5" fill="none"/></svg></div>
  <div class="abs arrow" style="top:1523px;left:1068px"><svg width="12" height="14"><path d="M3 2l6 5-6 5" stroke="#fff" stroke-width="2.5" fill="none"/></svg></div>
  <div class="abs project" style="top:1461px;left:131px"><div class="photo" role="img" aria-label="Finished home cinema with large screen and sofas" style="background:linear-gradient(160deg,#6a4a36,#2b1d16)"></div><h3>Residential Cinemas</h3></div>
  <div class="abs project" style="top:1461px;left:371px"><div class="photo" role="img" aria-label="Control room with a wall of monitors and office chairs" style="background:linear-gradient(160deg,#8c8a86,#3a3836)"></div><h3>Design And Consultations</h3></div>
  <div class="abs project" style="top:1461px;left:612px"><div class="photo" role="img" aria-label="Orange lounge with red chairs and wall television" style="background:linear-gradient(160deg,#f0a020,#b8581c)"></div><h3>Automated Lighting Control</h3></div>
  <div class="abs project" style="top:1461px;left:852px"><div class="photo" role="img" aria-label="Living room with fireplace, television and tablet controller" style="background:linear-gradient(160deg,#d8d4cc,#6a625a)"></div><h3>Outdoor Audio and Video</h3></div>
</section>

<section class="abs contact">
  <h2 class="abs head section-title" style="top:36px;left:0;color:#aaa"><span>Contact</span> Us</h2>

  <h3 class="abs col-title" style="top:110px;left:131px">FeedBack</h3>
  <div class="abs field" style="top:156px;left:131px">Name</div>
  <div class="abs field" style="top:213px;left:131px">Email</div>
  <div class="abs field" style="top:269px;left:131px">Phone</div>
  <div class="abs field" style="top:325px;left:131px;height:80px">Message</div>
  <div class="abs submit" style="top:419px;left:131px">SUBMIT</div>

  <h3 class="abs col-title" style="top:110px;left:560px">Contact Detail</h3>
  <div class="abs detail" style="top:150px;left:556px;width:300px">
    <div class="diamond"><svg width="44" height="44"><rect x="8" y="8" width="28" height="28" rx="4" transform="rotate(45 22 22)" fill="var(--orange)"/><path d="M22 14a6 6 0 0 1 6 6c0 4-6 10-6 10s-6-6-6-10a6 6 0 0 1 6-6z" fill="#fff"/><circle cx="22" cy="20" r="2" fill="var(--orange)"/></svg></div>
    <span>Lorem ipsum dolor sit amet, consectetuer adipiscing elit, sed diam nonummy nibh euismod.</span>
  </div>
  <div class="abs detail" style="top:231px;left:556px">
    <div class="diamond"><svg width="44" height="44"><rect x="8" y="8" width="28" height="28" rx="4" transform="rotate(45 22 22)" fill="var(--orange)"/><path d="M17 16c1-1 2-1 3 0l2 3-2 2c1 2 2 3 4 4l2-2 3 2c1 1 1 2 0 3-4 3-15-8-12-12z" fill="#fff"/></svg></div>
    <span>(555)-201-4830</span>
  </div>
  <div class="abs detail" style="top:293px;left:556px">
    <div class="diamond"><svg width="44" height="44"><rect x="8" y="8" width="28" height="28" rx="4" transform="rotate(45 22 22)" fill="var(--orange)"/><rect x="15" y="18" width="14" height="10" rx="1" fill="#fff"/><rect x="18" y="15" width="8" height="4" fill="none" stroke="#fff" stroke-width="1.5"/><rect x="18" y="21" width="8" height="4" fill="var(--orange)"/></svg></div>
    <span>(555)-201-4830</span>
  </div>
  <div class="abs detail" style="top:355px;left:556px">
    <div class="diamond"><svg width="44" height="44"><rect x="8" y="8" width="28" height="28" rx="4" transform="rotate(45 22 22)" fill="var(--orange)"/><rect x="15" y="17" width="14" height="10" fill="#fff"/><path d="M15 17l7 6 7-6" stroke="var(--orange)" stroke-width="1.5" fill="none"/></svg></div>
    <span>info@rwsoundworks.com</span>
  </div>

  <h3 class="abs col-title" style="top:110px;left:917px">Follow Us</h3>
  <div class="abs social" style="top:152px;left:913px"><svg width="44" height="44"><rect x="8" y="8" width="28" height="28" rx="4" transform="rotate(45 22 22)" fill="#1f5e96"/></svg>CIRCLEBOOK</div>
  <div class="abs social" style="top:211px;left:913px"><svg width="44" height="44"><rect x="8" y="8" width="28" height="28" rx="4" transform="rotate(45 22 22)" fill="#1bb4d0"/></svg>CHIRPER</div>
  <div class="abs social" style="top:270px;left:913px"><svg width="44" height="44"><rect x="8" y="8" width="28" height="28" rx="4" transform="rotate(45 22 22)" fill="#1a7fb8"/></svg>LINKWORK</div>
  <div class="abs social" style="top:330px;left:913px"><svg width="44" height="44"><rect x="8" y="8" width="28" height="28" rx="4" transform="rotate(45 22 22)" fill="#d9472e"/></svg>PLUSVINE</div>
</section>

<footer class="abs footer">© 2015 RW Soundworks. All rights reserved.</footer>

</body>
</html>
```